Business Card - Cooperate

Business Card for Larkfield Management Consulting

Target Market(s)

Corparte - b2B

Industry/Entity Type

Management Consulting - Professional Services

Contact Information for Business Card

Company Name , Slogan , Dummy Address,

Requirements
Must have
• Reach your Full Potential

```html
<!DOCTYPE html>
<html lang="en">
<head>
<meta charset="utf-8">
<title>Larkfield Management Consulting – Business Card</title>
<link rel="stylesheet" href="https://fonts.googleapis.com/css2?family=Nunito:wght@700&family=Open+Sans:wght@400;600;700&display=swap">
<style>
  :root {
    --backdrop: #2b2b2d;
    --front-glow: #7dc243;
    --front-mid: #2aa27f;
    --front-edge: #138c8a;
    --card-white: #ffffff;
    --card-shade: #f1f2f3;
    --brand-navy: #2c3a91;
    --brand-teal: #1a9a86;
    --rule: #6a6a98;
    --pin-green: #6cbf3e;
    --address-grey: #4a4a4a;
  }
  * { margin: 0; padding: 0; box-sizing: border-box; }
  html, body {
    width: 1200px;
    height: 900px;
    overflow: hidden;
    background: var(--backdrop);
  }
  .canvas {
    position: relative;
    width: 1200px;
    height: 900px;
    display: flex;
    flex-direction: column;
    align-items: center;
    justify-content: center;
    gap: 60px;
  }
  .card {
    position: relative;
    width: 560px;
    height: 320px;
    border-radius: 22px;
    overflow: hidden;
    box-shadow: 0 14px 30px rgba(0,0,0,0.45);
  }
  .card--front {
    background: radial-gradient(ellipse at 45% 45%, var(--front-glow) 0%, var(--front-mid) 45%, var(--front-edge) 100%);
  }
  .card--back {
    background: linear-gradient(135deg, var(--card-white) 0%, var(--card-shade) 100%);
  }
  .brand {
    position: absolute;
    display: flex;
    flex-direction: column;
  }
  .card--front .brand {
    left: 130px;
    top: 108px;
  }
  .card--back .brand {
    left: 90px;
    top: 70px;
  }
  .brand__row {
    display: flex;
    align-items: center;
    gap: 14px;
  }
  .brand__dot {
    width: 44px;
    height: 44px;
    border-radius: 50%;
  }
  .brand__name {
    font-family: "Nunito", sans-serif;
    font-weight: 700;
    font-size: 62px;
    line-height: 1;
    letter-spacing: 1px;
  }
  .brand__tagline {
    font-family: "Open Sans", sans-serif;
    font-weight: 700;
    font-size: 14px;
    letter-spacing: 3px;
    margin-top: 8px;
    margin-left: 58px;
  }
  .card--front .brand__dot { background: var(--card-white); }
  .card--front .brand__name { color: var(--card-white); }
  .card--front .brand__tagline { color: var(--card-white); }
  .card--back .brand__dot { background: var(--brand-navy); }
  .card--back .brand__name { color: var(--brand-navy); }
  .card--back .brand__tagline { color: var(--brand-teal); }
  .divider {
    position: absolute;
    left: 60px;
    right: 60px;
    top: 196px;
    height: 1px;
    background: var(--rule);
  }
  .address {
    position: absolute;
    left: 80px;
    top: 218px;
    display: flex;
    align-items: center;
    gap: 10px;
    font-family: "Open Sans", sans-serif;
    font-size: 16px;
    color: var(--address-grey);
  }
  .address svg { width: 14px; height: 20px; flex: none; }
</style>
</head>
<body>
  <main class="canvas">
    <section class="card card--front" aria-label="Card front">
      <div class="brand">
        <div class="brand__row">
          <span class="brand__dot"></span>
          <span class="brand__name">Larkfield</span>
        </div>
        <span class="brand__tagline">REACH YOUR FULL POTENTIAL</span>
      </div>
    </section>

    <section class="card card--back" aria-label="Card back">
      <div class="brand">
        <div class="brand__row">
          <span class="brand__dot"></span>
          <span class="brand__name">Larkfield</span>
        </div>
        <span class="brand__tagline">REACH YOUR FULL POTENTIAL</span>
      </div>
      <div class="divider"></div>
      <p class="address">
        <svg viewBox="0 0 14 20" aria-hidden="true">
          <path d="M7 0C3.1 0 0 3.1 0 7c0 5 7 13 7 13s7-8 7-13c0-3.9-3.1-7-7-7z" fill="var(--pin-green)"/>
          <circle cx="7" cy="7" r="2.6" fill="#ffffff"/>
        </svg>
        <span>11 dummy city, dummy place, P.O Box 0000 Dummy Land</span>
      </p>
    </section>
  </main>
</body>
</html>
```